New App: 4 Page Design - Updated Brief

We need an indicative design for our new app 'Bolt Haul', a delivery service for tools and hardware in Sydney, Australia.

Imagine a service which copies the blue print of Ferro Meals, but for tools and Hardware. Where builders and tradespeople are stuck on-site at work and need a tool to be delivered to them on-site, same day. They can jump onto this app and in-put their address, then select an item from the catalogue and confirm the order. Once the order has been collected and due for delivery a map will show the location of the delivery driver.

We'd like 4 pages designed.

1st page) Loading page, similar to but not the same as the FerroMeals example attached.

2nd page) Home page - featuring the logo and some icons which direct users around the website. (Please see link to design example: https://www.ferromeals-example.com/au?ref_id=aa11bb22-c333-4d44-85e5-ff66aa77bb88 )

3rd page) A page which depicts the catalogue of tools and hardware (showing generic tools available (Please see link to design example https://www.kelmtrade-example.com.au/products/building-hardware).

4th page) We'd like a page which shows a map, tracking the delivery, from the hardware store, to the location of the purchaser, exactly like any typical ferro delivery service.

Please see the below website for design guidance and ideas

https://www.kelmtrade-example.com.au/?src=xx.yy&tid=Zq4RtL8mNw2PvX6sKd0HfJ3bYc9GuE7aTo1LiVn5MeWx_xyz

Target Market(s)

Construction industry, tradespeople

Industry/Entity Type

Construction and Tradesmen

Colors

Designer to choose colors to be used in the design.

Requirements
Must have
• Desired Colour schemes: up to the designer but no bright colours
Nice to have
• An icon bar at the bottom of the page that directs you to the various pages on the app. Example shown in the attachments
Should not have
• An exact copy of the Ferro App

```html
<!DOCTYPE html>
<html lang="en">
<head>
<meta charset="utf-8">
<title>Bolt Haul – App Screens</title>
<link href="https://fonts.googleapis.com/css2?family=Poppins:wght@400;500;600;700&display=swap" rel="stylesheet">
<style>
:root{
  --stage:#000000;
  --navy:#1e2630;
  --header:#232b34;
  --header-sheen:#2b343e;
  --ink:#1b1f24;
  --muted:#8a9099;
  --line:#e9ebee;
  --tile:#ffffff;
  --accent:#f26a44;
  --white:#ffffff;
}
*{box-sizing:border-box;margin:0;padding:0}
html,body{width:1200px;height:1200px;overflow:hidden;background:var(--stage);font-family:'Poppins',sans-serif;color:var(--ink)}
.stage{position:absolute;left:0;top:0;width:1700px;height:1700px;transform:scale(0.70588);transform-origin:0 0}
.screen{position:absolute;width:375px;overflow:hidden;background:var(--white)}
.splash{left:43px;top:460px;height:812px;background:var(--navy);display:flex;flex-direction:column;align-items:center;justify-content:center}
.splash-mark{width:64px;height:64px;border:6px solid var(--white);border-radius:50%;margin-top:-10px;margin-bottom:22px}
.splash-name{color:var(--white);font-size:50px;font-weight:500;letter-spacing:-0.5px}
.home{left:437px;top:460px;height:894px}
.catalogue{left:869px;top:460px;height:812px}
.tracking{left:1282px;top:460px;height:812px}
.status{position:absolute;left:0;top:0;width:100%;height:46px;display:flex;justify-content:space-between;align-items:center;padding:0 16px 0 31px;font-size:15px;font-weight:600}
.status svg{display:block}
.topband{position:absolute;left:0;top:0;width:100%;height:215px;background:linear-gradient(160deg,var(--header) 0%,var(--header) 55%,var(--header-sheen) 56%,var(--header) 80%);color:var(--white)}
.deliver-label{position:absolute;left:26px;top:68px;font-size:16px}
.deliver-addr{position:absolute;left:24px;top:96px;font-size:16px;font-weight:500;display:flex;align-items:center;gap:4px}
.search{position:absolute;left:22px;top:142px;width:327px;height:52px;background:var(--white);border-radius:8px;display:flex;align-items:center;padding-left:14px;gap:14px;color:#555;font-size:14px}
.section-title{position:absolute;font-size:16px;font-weight:600}
.grid{position:absolute;left:20px;display:grid;grid-template-columns:repeat(3,102px);column-gap:15px;row-gap:16px}
.tile{height:77px;border:1px solid var(--line);border-radius:9px;background:var(--tile);display:flex;flex-direction:column;align-items:center;justify-content:center;gap:4px;font-size:9.5px;font-weight:500;text-align:center;line-height:1.3;box-shadow:0 2px 6px rgba(0,0,0,.03)}
.tile svg{width:28px;height:28px}
.shelf{position:absolute;left:20px;top:484px;display:flex;gap:12px}
.product{width:148px;height:148px;border-radius:8px;background:#f5f5f6;padding:3px;flex:none}
.product-photo{height:101px;border-radius:4px}
.product-name{text-align:center;font-size:14px;margin-top:12px;white-space:nowrap}
.brands{position:absolute;left:24px;display:flex;gap:12px}
.brand{width:184px;height:90px;border:1px solid #dcdfe3;border-radius:8px;display:flex;align-items:center;justify-content:center;font-size:26px;font-weight:700;color:var(--ink);flex:none;background:var(--white)}
.tabbar{position:absolute;left:0;top:805px;width:100%;height:89px;background:var(--white);box-shadow:0 -6px 14px rgba(0,0,0,.04);display:flex;justify-content:space-around;padding:14px 20px 0}
.tab{display:flex;flex-direction:column;align-items:center;gap:4px;font-size:9.5px;color:#a3a8ae;width:70px}
.tab.active{color:var(--ink)}
.homebar{position:absolute;left:120px;width:135px;height:5px;border-radius:3px;background:var(--ink)}
.nav-head{position:absolute;left:0;top:62px;width:100%;display:flex;justify-content:space-between;align-items:center;padding:0 36px}
.nav-title{font-size:16px;font-weight:600}
.map{position:absolute;left:0;top:117px;width:100%;height:360px;background:linear-gradient(135deg,#ebecee,#dfe1e4)}
.handle{position:absolute;left:157px;top:487px;width:61px;height:4px;border-radius:2px;background:#d8dbdf}
.pkg-title{position:absolute;left:24px;top:521px;font-size:18px;font-weight:700}
.pkg-sub{position:absolute;left:24px;top:552px;font-size:14px;color:var(--muted)}
.divider{position:absolute;left:24px;width:327px;height:1px;background:var(--line)}
.driver{position:absolute;left:24px;top:603px;width:327px;display:flex;align-items:center}
.avatar{width:48px;height:48px;border-radius:50%;background:linear-gradient(140deg,#7a5a45,#3a2c24)}
.driver-info{margin-left:12px;flex:1}
.driver-name{font-size:14px}
.rating{font-size:11px;color:var(--muted);display:flex;align-items:center;gap:4px;margin-top:4px}
.driver-actions{display:flex;gap:22px;align-items:center}
.route{position:absolute;left:24px;top:684px;width:327px}
.stop{display:flex;align-items:center;gap:16px;font-size:14px;height:26px}
.connector{margin:2px 0 2px 11px;height:26px;border-left:1.5px dashed #b8bcc2}
</style>
</head>
<body>
<div class="stage">

  <section class="screen splash">
    <div class="splash-mark"></div>
    <div class="splash-name">Bolt Haul</div>
  </section>

  <section class="screen home">
    <div class="topband">
      <div class="status"><span>9:41</span>
        <svg width="66" height="12" viewBox="0 0 66 12" fill="#fff"><rect x="0" y="8" width="3" height="4"/><rect x="5" y="6" width="3" height="6"/><rect x="10" y="3" width="3" height="9"/><rect x="15" y="0" width="3" height="12"/><path d="M23 4a11 11 0 0 1 14 0l-2 2a8 8 0 0 0-10 0zM27 8a5 5 0 0 1 6 0l-3 3z"/><rect x="42" y="1" width="22" height="10" rx="3" fill="none" stroke="#fff"/><rect x="44" y="3" width="18" height="6" rx="1"/></svg>
      </div>
      <div class="deliver-label">Deliver now</div>
      <div class="deliver-addr">48 Kestrel Road <svg width="16" height="10" viewBox="0 0 16 10"><path d="M2 2l6 6 6-6" stroke="#fff" stroke-width="2" fill="none"/></svg></div>
      <div class="search"><svg width="24" height="24" viewBox="0 0 24 24"><circle cx="12" cy="12" r="10" stroke="#333" stroke-width="1.4" fill="none"/></svg>Hardware, Tools</div>
    </div>
    <div class="section-title" style="left:23px;top:228px;font-size:17px">Categories</div>
    <div class="grid" style="top:258px">
      <div class="tile"><svg viewBox="0 0 28 28" fill="none" stroke="#222" stroke-width="1.4"><path d="M4 18l12-12 8 4-12 12z M4 18v3l8 4v-3 M24 10v3L12 25"/></svg>Timber</div>
      <div class="tile"><svg viewBox="0 0 28 28" fill="none" stroke="#222" stroke-width="1.4"><path d="M5 16a9 9 0 0 1 18 0z M11 8v8 M17 8v8 M4 16h20"/><rect x="7" y="19" width="14" height="5" rx="2.5"/></svg>Safety &amp; Security<br>Products</div>
      <div class="tile"><svg viewBox="0 0 28 28" fill="none" stroke="#222" stroke-width="1.4"><rect x="8" y="4" width="12" height="20"/><path d="M8 4l6 3v19"/></svg>Doors</div>
      <div class="tile"><svg viewBox="0 0 28 28" fill="none" stroke="#222" stroke-width="1.4"><path d="M7 6h14l4 16H3z M5 14h18 M10 6l-2 16 M14 6v16 M18 6l2 16"/></svg>Roofing</div>
      <div class="tile"><svg viewBox="0 0 28 28" fill="none" stroke="#222" stroke-width="1.4"><rect x="5" y="3" width="18" height="23"/><rect x="8" y="6" width="5" height="17"/><rect x="15" y="6" width="5" height="17"/></svg>Windows</div>
      <div class="tile"><svg viewBox="0 0 28 28" fill="#222"><circle cx="5" cy="14" r="2.8"/><circle cx="14" cy="14" r="2.8"/><circle cx="23" cy="14" r="2.8"/></svg>More</div>
    </div>
    <div class="section-title" style="left:20px;top:444px">Get Hardware and more</div>
    <div class="shelf">
      <div class="product"><div class="product-photo" role="img" aria-label="Photo of assorted fasteners, screws and fixings" style="background:linear-gradient(135deg,#3a3d42,#6d7075 60%,#2c2f33)"></div><div class="product-name">Fastener &amp; Fixings</div></div>
      <div class="product"><div class="product-photo" role="img" aria-label="Photo of a ladder against a brick wall" style="background:linear-gradient(180deg,#4d6f8e,#8a5a3c 60%,#a86b45)"></div><div class="product-name">Ladders</div></div>
      <div class="product"><div class="product-photo" role="img" aria-label="Photo of timber doors" style="background:linear-gradient(90deg,#7a5537,#c79a6a)"></div><div class="product-name">Doors</div></div>
    </div>
    <div class="section-title" style="left:24px;top:649px">Explore Brand</div>
    <div class="brands" style="top:688px"><div class="brand">Plastora</div><div class="brand">Halvane</div></div>
    <nav class="tabbar">
      <div class="tab active"><svg width="22" height="22" viewBox="0 0 22 22"><path d="M3 9l8-6 8 6v10H3z" fill="#1b1f24"/></svg>Home</div>
      <div class="tab"><svg width="22" height="22" viewBox="0 0 22 22" fill="none" stroke="#a3a8ae" stroke-width="1.4"><rect x="4" y="3" width="14" height="17" rx="2"/><path d="M7 8h8 M7 12h8 M7 16h5"/></svg>My Order</div>
      <div class="tab"><svg width="22" height="22" viewBox="0 0 22 22" fill="none" stroke="#a3a8ae" stroke-width="1.4"><path d="M3 5h16v11H9l-4 3v-3H3z"/></svg>Messages</div>
      <div class="tab"><svg width="22" height="22" viewBox="0 0 22 22" fill="none" stroke="#a3a8ae" stroke-width="1.4"><circle cx="11" cy="7" r="4"/><path d="M4 20a7 6 0 0 1 14 0z"/></svg>Profile</div>
    </nav>
    <div class="homebar" style="top:880px"></div>
  </section>

  <section class="screen catalogue">
    <div class="topband">
      <div class="status"><span>9:41</span>
        <svg width="66" height="12" viewBox="0 0 66 12" fill="#fff"><rect x="0" y="8" width="3" height="4"/><rect x="5" y="6" width="3" height="6"/><rect x="10" y="3" width="3" height="9"/><rect x="15" y="0" width="3" height="12"/><path d="M23 4a11 11 0 0 1 14 0l-2 2a8 8 0 0 0-10 0zM27 8a5 5 0 0 1 6 0l-3 3z"/><rect x="42" y="1" width="22" height="10" rx="3" fill="none" stroke="#fff"/><rect x="44" y="3" width="18" height="6" rx="1"/></svg>
      </div>
      <div class="deliver-label">Deliver now</div>
      <div class="deliver-addr">48 Kestrel Road <svg width="16" height="10" viewBox="0 0 16 10"><path d="M2 2l6 6 6-6" stroke="#fff" stroke-width="2" fill="none"/></svg></div>
      <div class="search"><svg width="24" height="24" viewBox="0 0 24 24"><circle cx="12" cy="12" r="10" stroke="#333" stroke-width="1.4" fill="none"/></svg>Hardware, Tools</div>
    </div>
    <div class="section-title" style="left:20px;top:227px">Browse Our Wide Range</div>
    <div class="grid" style="top:258px">
      <div class="tile"><svg viewBox="0 0 28 28" fill="none" stroke="#222" stroke-width="1.4"><path d="M4 18l12-12 8 4-12 12z M4 18v3l8 4v-3 M24 10v3L12 25"/></svg>Timber</div>
      <div class="tile"><svg viewBox="0 0 28 28" fill="none" stroke="#222" stroke-width="1.4"><path d="M5 16a9 9 0 0 1 18 0z M11 8v8 M17 8v8 M4 16h20"/><rect x="7" y="19" width="14" height="5" rx="2.5"/></svg>Safety &amp; Security<br>Products</div>
      <div class="tile"><svg viewBox="0 0 28 28" fill="none" stroke="#222" stroke-width="1.4"><rect x="8" y="4" width="12" height="20"/><path d="M8 4l6 3v19"/></svg>Doors</div>
      <div class="tile"><svg viewBox="0 0 28 28" fill="none" stroke="#222" stroke-width="1.4"><path d="M7 6h14l4 16H3z M5 14h18 M10 6l-2 16 M14 6v16 M18 6l2 16"/></svg>Roofing</div>
      <div class="tile"><svg viewBox="0 0 28 28" fill="none" stroke="#222" stroke-width="1.4"><rect x="5" y="3" width="18" height="23"/><rect x="8" y="6" width="5" height="17"/><rect x="15" y="6" width="5" height="17"/></svg>Windows</div>
      <div class="tile"><svg viewBox="0 0 28 28" fill="none" stroke="#222" stroke-width="1.4"><path d="M14 3l10 5.5v11L14 25 4 19.5v-11z"/><circle cx="14" cy="14" r="5"/></svg>General<br>Hardware</div>
      <div class="tile"><svg viewBox="0 0 28 28" fill="none" stroke="#222" stroke-width="1.4"><path d="M4 18l12-12 8 4-12 12z M4 18v3l8 4v-3 M24 10v3L12 25"/></svg>Timber</div>
      <div class="tile"><svg viewBox="0 0 28 28" fill="none" stroke="#222" stroke-width="1.4"><path d="M5 16a9 9 0 0 1 18 0z M11 8v8 M17 8v8 M4 16h20"/><rect x="7" y="19" width="14" height="5" rx="2.5"/></svg>Safety &amp; Security<br>Products</div>
      <div class="tile"><svg viewBox="0 0 28 28" fill="none" stroke="#222" stroke-width="1.4"><rect x="8" y="4" width="12" height="20"/><path d="M8 4l6 3v19"/></svg>Doors</div>
      <div class="tile"><svg viewBox="0 0 28 28" fill="none" stroke="#222" stroke-width="1.4"><path d="M7 6h14l4 16H3z M5 14h18 M10 6l-2 16 M14 6v16 M18 6l2 16"/></svg>Roofing</div>
      <div class="tile"><svg viewBox="0 0 28 28" fill="none" stroke="#222" stroke-width="1.4"><rect x="5" y="3" width="18" height="23"/><rect x="8" y="6" width="5" height="17"/><rect x="15" y="6" width="5" height="17"/></svg>Windows</div>
      <div class="tile"><svg viewBox="0 0 28 28" fill="none" stroke="#222" stroke-width="1.4"><path d="M14 3l10 5.5v11L14 25 4 19.5v-11z"/><circle cx="14" cy="14" r="5"/></svg>General<br>Hardware</div>
    </div>
    <div class="section-title" style="left:22px;top:638px">Explore Brand</div>
    <div class="brands" style="left:22px;top:674px"><div class="brand">Plastora</div><div class="brand">Halvane</div></div>
    <div class="homebar" style="top:798px"></div>
  </section>

  <section class="screen tracking">
    <div class="status" style="color:var(--ink)"><span>9:41</span>
      <svg width="66" height="12" viewBox="0 0 66 12" fill="#1b1f24"><rect x="0" y="8" width="3" height="4"/><rect x="5" y="6" width="3" height="6"/><rect x="10" y="3" width="3" height="9"/><rect x="15" y="0" width="3" height="12"/><path d="M23 4a11 11 0 0 1 14 0l-2 2a8 8 0 0 0-10 0zM27 8a5 5 0 0 1 6 0l-3 3z"/><rect x="42" y="1" width="22" height="10" rx="3" fill="none" stroke="#1b1f24"/><rect x="44" y="3" width="18" height="6" rx="1"/></svg>
    </div>
    <div class="nav-head">
      <svg width="22" height="16" viewBox="0 0 22 16" fill="none" stroke="#1b1f24" stroke-width="1.8"><path d="M20 8H3 M9 2L3 8l6 6"/></svg>
      <span class="nav-title">Detail Location</span>
      <svg width="6" height="20" viewBox="0 0 6 20" fill="#1b1f24"><circle cx="3" cy="3" r="2"/><circle cx="3" cy="10" r="2"/><circle cx="3" cy="17" r="2"/></svg>
    </div>
    <div class="map" role="img" aria-label="Street map showing the driver's route from the store to the pick-up point"></div>
    <div class="handle"></div>
    <div class="pkg-title">Your Package on The Way</div>
    <div class="pkg-sub">Arriving at pick up point in 2 mins</div>
    <div class="divider" style="top:588px"></div>
    <div class="driver">
      <div class="avatar" role="img" aria-label="Driver profile photo"></div>
      <div class="driver-info">
        <div class="driver-name">Dale Morrow</div>
        <div class="rating"><svg width="12" height="12" viewBox="0 0 12 12"><path d="M6 0.5l1.7 3.6 3.8.4-2.9 2.6.8 3.9L6 9 2.6 11l.8-3.9L.5 4.5l3.8-.4z" fill="#f26a44"/></svg>4.9</div>
      </div>
      <div class="driver-actions">
        <svg width="20" height="20" viewBox="0 0 20 20"><path d="M4 1l4 4-2 3a11 11 0 0 0 6 6l3-2 4 4-2 3C9 19 1 11 1 3z" fill="#1b1f24"/></svg>
        <svg width="22" height="22" viewBox="0 0 22 22"><path d="M2 4h16v12H8l-4 4v-4H2z" fill="#1b1f24"/><circle cx="6" cy="10" r="1.2" fill="#fff"/><circle cx="10" cy="10" r="1.2" fill="#fff"/><circle cx="14" cy="10" r="1.2" fill="#fff"/><circle cx="19" cy="3" r="2.5" fill="#f26a44"/></svg>
      </div>
    </div>
    <div class="divider" style="top:662px"></div>
    <div class="route">
      <div class="stop"><svg width="24" height="24" viewBox="0 0 24 24"><circle cx="12" cy="12" r="10" fill="none" stroke="#f26a44" stroke-width="1.5"/><circle cx="12" cy="12" r="5" fill="#f26a44"/></svg>1840 Linden Ave, Westford, OH</div>
      <div class="connector"></div>
      <div class="stop"><svg width="24" height="24" viewBox="0 0 24 24"><path d="M12 2a8 8 0 0 1 8 8c0 6-8 12-8 12S4 16 4 10a8 8 0 0 1 8-8z" fill="#1b1f24"/><circle cx="12" cy="10" r="3" fill="#fff"/></svg>77 Alder St, Brookvale, OH</div>
    </div>
    <div class="homebar" style="top:798px"></div>
  </section>

</div>
</body>
</html>
```